company name - KELBRIDGE AIRPORT TRANSFER.
include this information please .....25 YEARS EXPERIENCE / CARS+MPVS+MINIBUSES AVAILABLE - ALL AT SAME PRICE AT ANY TIME OF DAY. NO EXTRA HIDDEN CHARGES.

PRICES [ selection ] ......

DUNMARSH ....£100
PELLORN ....£130
VASKE...£55.00
ORMBRIDGE ...£60.00
WESTHALLOCK ...£100.00
NORTH FELWAY ...£100,00
QUAY AIRPORT ...£95.00

```html
<!DOCTYPE html>
<html lang="en">
<head>
<meta charset="utf-8">
<title>Kelbridge Airport Transfer – Flyer</title>
<link rel="stylesheet" href="https://fonts.googleapis.com/css2?family=Lexend:wght@300;400;600&display=swap">
<style>
  :root {
    --page-bg: #e9edf2;
    --paper: #ffffff;
    --paper-fade: #e4e7ec;
    --brand-blue: #2f63ad;
    --brand-orange: #f7941d;
    --sky-deep: #1f5fb4;
    --sky-top: #3f84d6;
    --sky-mid: #8cbbe8;
    --haze: rgba(255, 255, 255, 0.85);
    --steel: rgba(205, 214, 226, 0.9);
    --navy-suit: rgba(30, 42, 70, 0.55);
    --divider: #c9d3e0;
  }
  * { margin: 0; padding: 0; box-sizing: border-box; }
  html, body {
    width: 1040px; height: 1200px; overflow: hidden;
    background: var(--page-bg);
    font-family: "Lexend", "Century Gothic", sans-serif;
  }
  .flyer {
    position: absolute; left: 126px; top: 41px;
    width: 788px; height: 1118px;
    background: linear-gradient(to bottom, var(--paper) 70%, var(--paper-fade) 100%);
    box-shadow: 0 18px 40px rgba(40, 60, 90, 0.25);
    overflow: hidden;
  }
  .hero-photo {
    position: absolute; left: 0; top: 0; width: 788px; height: 517px;
    background:
      radial-gradient(ellipse 240px 320px at 78% 62%, var(--navy-suit), transparent 70%),
      radial-gradient(ellipse 300px 420px at 92% 40%, var(--steel), transparent 75%),
      radial-gradient(ellipse 340px 120px at 28% 78%, var(--haze), transparent 75%),
      radial-gradient(ellipse 180px 380px at 6% 60%, rgba(40, 110, 190, 0.7), transparent 75%),
      linear-gradient(170deg, var(--sky-deep) 0%, var(--sky-top) 35%, var(--sky-mid) 75%, #dbe9f6 100%);
  }
  .title-box {
    position: absolute; left: 70px; top: 497px; width: 651px; height: 79px;
    display: flex; align-items: center; justify-content: space-between;
    padding: 0 8px 0 8px;
    border: 2px solid var(--brand-blue);
    background: var(--paper);
    font-weight: 600; font-size: 37px; letter-spacing: -0.5px; white-space: nowrap;
  }
  .title-box .name { color: var(--brand-blue); }
  .title-box .service {
    background: var(--brand-orange); color: var(--paper);
    padding: 4px 10px;
  }
  .selling-points { position: absolute; left: 70px; top: 612px; color: var(--brand-orange); }
  .selling-points p { white-space: nowrap; }
  .experience { font-weight: 600; font-size: 36px; line-height: 52px; }
  .fleet { font-weight: 600; font-size: 34.5px; line-height: 52px; }
  .fleet .light { font-weight: 300; }
  .terms { font-weight: 300; font-size: 29px; line-height: 37px; }
  .prices { position: absolute; top: 817px; left: 0; width: 788px; color: var(--brand-blue); }
  .price-col { position: absolute; top: 0; list-style: none; font-weight: 300; font-size: 26px; line-height: 47px; white-space: nowrap; }
  .price-col.left { left: 70px; }
  .price-col.right { left: 446px; }
  .price-col .label { font-weight: 600; font-size: 25px; }
  .price-divider { position: absolute; left: 376px; top: 8px; width: 1px; height: 159px; background: var(--divider); }
  .cta {
    position: absolute; left: 70px; top: 1024px; width: 651px; height: 94px;
    background: var(--brand-orange); color: var(--paper);
    display: flex; align-items: center; justify-content: center;
    font-size: 52px; font-weight: 300; white-space: nowrap;
  }
  .cta .phone { font-weight: 600; margin-left: 12px; }
</style>
</head>
<body>
  <main class="flyer">
    <div class="hero-photo" role="img" aria-label="Businessman with a suitcase checking his watch among glass skyscrapers as a passenger jet flies overhead"></div>

    <h1 class="title-box">
      <span class="name">KELBRIDGE</span>
      <span class="service">AIRPORT TRANSFER</span>
    </h1>

    <section class="selling-points">
      <p class="experience">25 YEARS EXPERIENCE</p>
      <p class="fleet">CARS+MPVS+MINIBUSES <span class="light">AVAILABLE –</span></p>
      <p class="terms">ALL AT SAME PRICE AT ANY TIME OF DAY</p>
      <p class="terms">NO EXTRA HIDDEN CHARGES</p>
    </section>

    <section class="prices">
      <ul class="price-col left">
        <li class="label">Prices:</li>
        <li>DUNMARSH £100</li>
        <li>PELLORN £130</li>
        <li>VASKE £55</li>
      </ul>
      <div class="price-divider"></div>
      <ul class="price-col right">
        <li>ORMBRIDGE £60</li>
        <li>WESTHALLOCK £100</li>
        <li>NORTH FELWAY £100</li>
        <li>QUAY AIRPORT £95</li>
      </ul>
    </section>

    <div class="cta">Call to book<span class="phone">741 552 308</span></div>
  </main>
</body>
</html>
```